Promotional Poster for Music Achievement Program

I need a vertical 11x17 poster designed for a new program called Bright Path Music Achievement Program. The poster will be displayed in the lesson rooms and lobbies of music schools who use this program. The main headline of the flyer should be "Ask your teacher about Bright Path" And then the additional text should be "Love your lessons and practice like never before with 10 levels of achievement!" I would like to use the logo on the flyer, which I uploaded here. In terms of artwork/design, I am looking for a fun, but clean feel. The purpose of the program is for students to progress through ten levels of achievement as they climb higher and higher to mastery of their instrument at level 10, so a feel of climbing, leveling up, or advancing would be good. And of course, this is a music program, so any musical artwork involved would make sense. But again - nothing too busy or overwhelming!

Target Market(s)

Parents waiting in the lobby of a music school.

Industry/Entity Type

Promotional

Colors

Designer to choose colors to be used in the design.

Requirements
Must have
• - Bright Path logo
• - This headline: Ask your teacher about Bright Path
• - This additional text: Love your lessons and practice like never before with 10 levels of achievement!
Nice to have
• In terms of artwork/design, I am looking for a fun, but clean feel. The purpose of the program is for students to progress through ten levels of achievement as they climb higher and higher to mastery of their instrument at level 10, so a feel of climbing, leveling up, or advancing would be good. And of course, this is a music program, so any musical artwork involved would make sense. But again - nothing too busy or overwhelming!
Should not have
• Should not be too busy.

```html
<!DOCTYPE html>
<html lang="en">
<head>
<meta charset="utf-8">
<title>Bright Path Music Achievement Program</title>
<link href="https://fonts.googleapis.com/css2?family=Jost:wght@400&family=Arimo:wght@400;700&display=swap" rel="stylesheet">
<style>
  :root {
    --paper: #f7f4bd;
    --headline-red: #b2151f;
    --band-red: #b5121b;
    --brick-brown: #7f5235;
    --quote-brown: #7a5233;
    --body-ink: #4a3b2e;
    --logo-ink: #2b2b2b;
    --white: #ffffff;
  }
  * { margin: 0; padding: 0; box-sizing: border-box; }
  html, body { width: 777px; height: 1200px; overflow: hidden; background: var(--paper); }
  .poster { position: relative; width: 777px; height: 1200px; background: var(--paper); overflow: hidden; }

  .brand {
    position: absolute; top: 68px; right: 40px;
    display: flex; align-items: center; gap: 10px;
    font-family: "Arimo", sans-serif; font-weight: 700; font-size: 34px;
    color: var(--logo-ink);
  }
  .brand-square { width: 22px; height: 22px; background: var(--headline-red); }

  .headline {
    position: absolute; left: 48px; top: 196px;
    font-family: "Jost", sans-serif; font-weight: 400;
    color: var(--headline-red); text-transform: uppercase;
    font-size: 82px; line-height: 80px; letter-spacing: 1px;
    z-index: 2;
  }
  .headline span { display: block; }
  .headline .name { font-size: 64px; letter-spacing: 0; }

  .tagline {
    position: absolute; left: 48px; top: 545px; width: 390px;
    font-family: "Arimo", sans-serif; font-size: 19.5px; line-height: 29px;
    color: var(--body-ink);
  }
  .tagline p { padding-left: 44px; }
  .quote-mark {
    position: absolute; font-family: Georgia, serif; font-weight: 700;
    font-size: 78px; line-height: 1; color: var(--quote-brown);
  }
  .quote-open { left: 0; top: -8px; }
  .quote-close { left: 214px; top: 66px; }

  .guitarist {
    position: absolute; left: 448px; top: 280px; width: 184px; height: 316px;
    background: linear-gradient(180deg, #efe7b2 0%, #e9c98f 60%, #d8a76f 100%);
    border-radius: 6px; z-index: 1;
  }

  .level-bars { position: absolute; left: 0; top: 0; }
  .level-bars rect { fill: var(--brick-brown); }

  .footer-band {
    position: absolute; left: 0; bottom: 0; width: 777px; height: 58px;
    background: var(--band-red); color: var(--white);
    font-family: "Jost", sans-serif; font-size: 30px; letter-spacing: 1.2px;
    display: flex; align-items: center; justify-content: center;
  }
</style>
</head>
<body>
<main class="poster">
  <div class="brand"><span class="brand-square"></span><span>Bright Path</span></div>

  <h1 class="headline">
    <span>Ask your</span>
    <span>teacher</span>
    <span>about</span>
    <span class="name">Bright Path</span>
  </h1>

  <div class="tagline">
    <span class="quote-mark quote-open">&ldquo;</span>
    <p>Love your lessons and practice like never before with 10 levels of achievement!</p>
    <span class="quote-mark quote-close">&rdquo;</span>
  </div>

  <div class="guitarist" role="img" aria-label="Pixel-art guitarist giving a rock sign, standing on top of the tallest bar"></div>

  <svg class="level-bars" width="777" height="1142" viewBox="0 0 777 1142" aria-hidden="true">
    <defs>
      <rect id="brick" width="78" height="22"/>
    </defs>
    <!-- column 1: 6 bricks -->
    <g transform="translate(30,0)">
      <use href="#brick" y="1106"/><use href="#brick" y="1067"/><use href="#brick" y="1028"/>
      <use href="#brick" y="989"/><use href="#brick" y="950"/><use href="#brick" y="911"/>
    </g>
    <!-- column 2: 5 bricks -->
    <g transform="translate(121,0)">
      <use href="#brick" y="1106"/><use href="#brick" y="1067"/><use href="#brick" y="1028"/>
      <use href="#brick" y="989"/><use href="#brick" y="950"/>
    </g>
    <!-- column 3: 9 bricks -->
    <g transform="translate(212,0)">
      <use href="#brick" y="1106"/><use href="#brick" y="1067"/><use href="#brick" y="1028"/>
      <use href="#brick" y="989"/><use href="#brick" y="950"/><use href="#brick" y="911"/>
      <use href="#brick" y="872"/><use href="#brick" y="833"/><use href="#brick" y="794"/>
    </g>
    <!-- column 4: 6 bricks -->
    <g transform="translate(303,0)">
      <use href="#brick" y="1106"/><use href="#brick" y="1067"/><use href="#brick" y="1028"/>
      <use href="#brick" y="989"/><use href="#brick" y="950"/><use href="#brick" y="911"/>
    </g>
    <!-- column 5: 7 bricks -->
    <g transform="translate(394,0)">
      <use href="#brick" y="1106"/><use href="#brick" y="1067"/><use href="#brick" y="1028"/>
      <use href="#brick" y="989"/><use href="#brick" y="950"/><use href="#brick" y="911"/>
      <use href="#brick" y="872"/>
    </g>
    <!-- column 6: 14 bricks (summit) -->
    <g transform="translate(486,0)">
      <use href="#brick" y="1106"/><use href="#brick" y="1067"/><use href="#brick" y="1028"/>
      <use href="#brick" y="989"/><use href="#brick" y="950"/><use href="#brick" y="911"/>
      <use href="#brick" y="872"/><use href="#brick" y="833"/><use href="#brick" y="794"/>
      <use href="#brick" y="755"/><use href="#brick" y="716"/><use href="#brick" y="677"/>
      <use href="#brick" y="638"/><use href="#brick" y="599"/>
    </g>
    <!-- column 7: 9 bricks -->
    <g transform="translate(577,0)">
      <use href="#brick" y="1106"/><use href="#brick" y="1067"/><use href="#brick" y="1028"/>
      <use href="#brick" y="989"/><use href="#brick" y="950"/><use href="#brick" y="911"/>
      <use href="#brick" y="872"/><use href="#brick" y="833"/><use href="#brick" y="794"/>
    </g>
    <!-- column 8: 5 bricks -->
    <g transform="translate(668,0)">
      <use href="#brick" y="1106"/><use href="#brick" y="1067"/><use href="#brick" y="1028"/>
      <use href="#brick" y="989"/><use href="#brick" y="950"/>
    </g>
  </svg>

  <footer class="footer-band">Bright Path Music Achievement Program.</footer>
</main>
</body>
</html>
```